Web Design Peartreegrove

Overview: To develop web site with 1 main page and 1 sample inside page. Site already exists, but has been put offline. Content has been fully rewritten. If I like your style, I will pay extra for additional inside pages.
WHO I AM?
www.peartreegrove.example was originally created to become an online community for people to use my online tools, researches, and findings to learn how to become happier.
Today, my primary services is “health coaching and lifestyle specialist.” I’m a food specialist suggesting customized solutions for my clients to eat better, how to eat, cook, groceries shop, lose weight, reduce craving, and reverse diseases.
My edge is when a suggest food I explain Why such food hurts them (or make them sick –or reason of diseases) or how the food I suggest can heal them, strengthen them, or make them lose weight. My connection to food is medical and directly impacts my client’s health.
I want to be seen as a professional in clinical nutrition and as a guru in overall wellbeing.
I coach my clients’ lifestyle as a WHOLE, introducing them to new food, fitness, and teaching them techniques to better cope with life. I study their overall health, history, and treatments, diseases, allergies as a WHOLE, connecting all medical specialties.
My services:
I sell coaching sessions, for 1 hour, 2/month for a total program of 6 months. During the sessions, I not only coach client on nutrition, but also on career, relationship, fitness, goals, and the reasons why people can’t achieve their dreams, or how to remove stress or re-organize their lives.
Future services: I may want to sell products such as T-shirts and other promotional items
Payment methods: Since I sell, I’ll need coinlatch and credit card payment on line. I accept checks as well (they can find my address on “contact us”)
More services, near future:
As a Certified personal fitness Trainer, I will soon offer circuit training (outdoors) and boot camps in the neighborhood to get people moving, at very affordable prices. The goal of those events will be to grow my peartreegrove community and get new clients for Health coaching.
Knowledgeable about controlling the mind, anger, and stress, I will soon offer group meditations and breathing sessions .
Objectives:
The goal of the site are:
• To entice visitors to become my clients. The look of the site needs to reflect my customized services.
• To offer to spend an hour with client for a free health history.
• To post videos about cooking videos, discussing a theme (sugar craving, which Carbs is good for me?)
• After I meet people and give them my business cards, as they visit my site, they needs to feel impressed by the caliber of expertise.
Schedules and Budget:
Target due date is 1 week from submission of my project. During that phase, I’d like to see a wireframe, colors, styles, incorporating my logo, suggesting pictures. I would like designed tabs, access to videos, and photo library.
Motivations for people to become CLIENTS:
I think what would make people want to get my services is if they see me as an expert in holistic weight loss, someone that they can share their life, thrust, and speak at length without being judged. Visuals are crucial to simply explain effect of food on the body (needs videos main page and archive videos on various topics)
Overall, the emotions we can play with - (key words) feeling energized, feeling strong, in control of your life, a holitistic approach to a new healthy lifestyle, Balance mind, fitness, and diet, take responsibility for your own life, feeling lighter, happier, more peaceful.
Key issues of my clients:
Weight issues, high blood pressure, depression, anxiety, stress, don’t know and what to cook, suffer from diabetes, celiac, digestive diseases. People are fatigued or can’t sleep. They are addicted to sugar, coffee, fast food, speedy life.
Another issue is finding time to eat better, making exercise a routine, making the time to remove stress and enjoy life.
How do I solve clients’ problems?:
Rather than being treated by various medical specialists, I look over their Overall health since childhood. I try to find triggers of their sicknesses that often originate from their lifestyle (stress, lack of exercise, eating junk, allergies) and I recommend life modification, introduce new food, exercise , and help them shuffle their lives around. My approach is extremely customized and always requires Hours of research on my side to fully guide a client.
Demographics:
Teenagers, singles, families, young mothers. Most of clients come with weight issues, some may come to reduce cravings.
Key Messages:
The main page (please find attached “wireframe”) shall give the visitor a sense he found the guru in holistic health. Whatever medical concern they have or struggle will finally be taken care of. Someone loves them and truly cares. Food knowledge is medical, flavor, and based on client’s own taste and willingness to try. The overall feel needs to be sleek and professional.
Call to Action
Ideally, I want people to e-mail me their filled up health history (can download blank men or women health history form) so I can schedule an appointment with them (the best solution for me)
People can also call me. Since calling me is for general questions about my program, I would prefer the e-mail version whereby clients send me their health history.
Creative Considerations
Layout – considerations in accordance to brand guidelines
Need suggetions!
Tone –
Expert in clinical food and holistic health.
Visual
Color palette : I’m not sure, but the background could be light gray (clinical health), golden desert, sahara desert, earthy, pottery (well being) warm colors (orange to warm brown) or other suggestion?
Photography: I thought about flash picture. 1 picture as banner with a message on it. About 3 pictures rotate randomly.
Picture A: is “holistic food, green vegetables, natural edible roots, or cruciferous vegetables, a platter of fresh fruits and vegies, or fresh market (spices, roots, fruits and vegies). Picture needs to be crisp clear.
Picture B: Ideally: a lady fitness trainer training group exercise outdoors, in a park, or a group of people exercising outside, people look happy, boot camp training, circuit training as a group
Picture C: a picture representing the soul ,meditation, a person relaxing next to beach or in forest, next to flowers or lushy plants, a person re-energizing.
Logo: attached as separate files with various backgrounds
Icons: may look cool to use vegies or weight, happy face, or ginger root…
typography, graphics: need suggestions!

Resources
• I have an existing website name “peartreegrove.example” the site has been put out of internet since we were trying to change it. Let me know if you need to access site. Content of the site is ineffective.
• All content has been written. You can suggest layouts and tabs
Updates

Target Market(s)

My industry is Health care, holistic Health (no medications, no supplements, no surgeries)
Buyer’s Type could be anyone wanting to lose weight, feel better, reduce stress, learn to eat, to cook, to groceries shop. My buyers are confused about all diets.My audience is people WHO WANT change in their lives. Some people know they should eat better, they mostly need support and motivation.
Typical buyer is someone who wants a new chance, a new life!
My primary target buyer is:
1. Family. I wish to coach the entire family into healthier eating and teach them how to cook and eat as a family by changing their habits.
My secondary markets are:
1.Teenagers (often eating emotionally and confused about diets)

Industry/Entity Type

Requirements
Must have
• • Format – web, print, video, sound
I would like videos (clipvane connect) – friendloom connect – calendar (I will update) – I will update my content, videos, and photo library regularly – people should be able to e-mail me from site – maybe be able to go through web conference. 2 different words or pdf forms shall be available for download or online filling, then they should be able to e-mail forms through site or through their personal mail system. They can also print and mail it to me.
Managing the site:
I would like to upload videos, pictures and text freely and easily. I would like to manage and update content
Nice to have
• would look cool to use entire background as a super picture!

```html
<!DOCTYPE html>
<html lang="en">
<head>
<meta charset="utf-8">
<title>Peartreegrove – Balanced Nutrition, Mind, and Fitness</title>
<link href="https://fonts.googleapis.com/css2?family=Archivo+Black&family=Ubuntu:wght@400;500;700&family=Oswald:wght@500&family=Cormorant+Garamond:ital,wght@1,500;1,600&family=Dosis:wght@500;600&display=swap" rel="stylesheet">
<style>
:root{
  --red-deep:#8e1206;
  --red:#b5200d;
  --red-bright:#c9340f;
  --orange:#d9540f;
  --orange-light:#f07a1c;
  --orange-text:#e8690c;
  --frame:#6e0c05;
  --green:#5aa512;
  --green-light:#7cc51f;
  --green-dark:#3f7d0a;
  --ink:#2c2c2c;
  --grey:#555;
  --white:#fff;
  --cream:#f3e9df;
}
*{box-sizing:border-box;margin:0;padding:0}
html,body{width:1200px;height:900px;overflow:hidden}
body{position:relative;background:var(--white);font-family:Arial,Helvetica,sans-serif;color:var(--ink)}
.abs{position:absolute}

/* header */
.brand{left:115px;top:10px;display:flex;flex-direction:column}
.brand-row{display:flex;align-items:center;gap:10px}
.brand-dot{width:54px;height:54px;border-radius:50%;background:var(--green)}
.brand-name{font-family:Ubuntu,sans-serif;font-weight:500;font-size:31px;color:#1d1d1b;letter-spacing:-.5px}
.brand-tag{font-family:Ubuntu,sans-serif;font-size:8.5px;font-weight:700;color:#333;margin:-6px 0 0 68px;letter-spacing:.3px}
.nav{left:395px;top:8px;width:698px;height:70px;display:flex;border-radius:7px;overflow:hidden;background:linear-gradient(var(--orange-light),var(--red-bright) 60%,var(--red-deep));box-shadow:0 0 0 2px #b6370c}
.nav a{flex:1;display:flex;justify-content:center;padding-top:20px;text-align:center;font-family:"Archivo Black",sans-serif;font-size:13px;line-height:15px;color:#2a0a00;text-decoration:none;border-right:1px solid rgba(80,10,0,.45)}
.nav a:last-child{border-right:0}
.nav a.current{background:linear-gradient(#ffb13a,#f27a1a 55%,#c9340f)}
.nav-pointer{left:736px;top:8px}

/* red band */
.band{left:0;top:82px;width:1200px;height:368px;background:repeating-linear-gradient(45deg,rgba(0,0,0,.04) 0 2px,transparent 2px 6px),radial-gradient(ellipse at 70% 50%,var(--red-bright),var(--red) 60%,var(--red-deep))}
.hero{left:125px;top:93px;width:675px;height:349px;border:5px solid var(--frame);background:linear-gradient(90deg,#f1ece6,#faf7f3 60%,#efe6dc);}
.hero-photo{position:absolute;inset:0;background:radial-gradient(ellipse 45% 35% at 45% 70%,#d6b09a,transparent 70%),radial-gradient(ellipse 25% 20% at 40% 78%,#3fa68a,transparent 70%)}
.hero-quote{position:absolute;left:385px;top:32px;font-family:"Cormorant Garamond",serif;font-style:italic;font-weight:600;font-size:25px;line-height:21px;color:#1b1b1b}
.hero-quote .mark{color:var(--red);font-size:30px}
.hero-pointer{left:236px;top:442px}

.signup{left:808px;top:93px;width:285px;height:240px;border-radius:5px;background:linear-gradient(var(--orange-light),var(--orange) 40%,var(--red-bright));box-shadow:0 2px 6px rgba(0,0,0,.4)}
.signup h2{font-family:Ubuntu,sans-serif;font-weight:500;font-size:18px;color:var(--white);padding:12px 0 0 12px;height:46px;border-bottom:1px solid rgba(255,255,255,.35)}
.field{position:absolute;left:11px;width:262px;height:27px;background:var(--white);border-radius:3px;display:flex;align-items:center;gap:7px;padding:0 8px;font-size:11px;color:#222}
.field .end{margin-left:auto}
.social{position:absolute;left:11px;top:192px;width:262px;height:30px;background:var(--white);border-radius:3px;display:flex;align-items:center;gap:4px;padding:0 3px}
.social span{height:18px;display:flex;align-items:center;gap:3px;padding:0 4px;font-size:7px;color:var(--white);border-radius:2px}
.s-friend{background:#3d5a9a}
.s-chirp{background:#2ea5d6}
.s-box{width:9px;height:9px;background:var(--white)}
.continue{margin-left:auto;height:26px;width:68px;background:linear-gradient(#f39a3a,#c95a12);border:1px solid #8a3b08;border-radius:2px;font-size:9px;color:#3a1500;display:flex;align-items:center;justify-content:center;gap:4px}
.join{left:810px;top:335px;width:281px;height:103px;border-radius:6px;background:linear-gradient(#b21a0d,#9a0e06 55%,#7e0903);box-shadow:0 3px 6px rgba(0,0,0,.5);text-align:center}
.join .lead{font-family:"Cormorant Garamond",serif;font-style:italic;font-weight:500;font-size:27px;color:var(--cream);padding-top:8px}
.join .cta{font-family:Oswald,sans-serif;font-size:33px;color:#f59a23;margin-top:2px;display:flex;justify-content:center;align-items:center;gap:12px}

/* strip */
.strip{left:0;top:450px;width:1200px;height:63px;background:var(--red-bright)}
.thumb{position:absolute;top:457px;width:62px;height:50px;border:3px solid var(--white);box-shadow:0 0 0 1px #888}
.strip-text{left:443px;top:466px;font-family:Ubuntu,sans-serif;font-size:23px;color:var(--white)}
.strip-text em{font-style:normal;color:#f9a23a}
.auth{left:869px;top:468px;font-family:Dosis,sans-serif;font-weight:600;font-size:20px;color:var(--white);letter-spacing:.5px}
.auth b{display:inline-block;width:3px;height:17px;background:var(--white);margin:0 9px;vertical-align:-2px}

/* content */
.h-col{font-family:Ubuntu,sans-serif;font-size:23px;color:#333;letter-spacing:-.3px}
.h-side{font-family:Ubuntu,sans-serif;font-weight:700;font-size:17px;color:#333}
.vdiv{width:0;border-left:1px dashed #999}
.body-s{font-size:11px;line-height:14.5px;color:#222}
.lead-o{font-weight:700;font-size:12px;line-height:14px;color:var(--orange-text)}
.btn-green{display:flex;align-items:center;justify-content:center;border-radius:8px;background:linear-gradient(var(--green-light),var(--green));border:1px solid var(--green-dark);font-family:Ubuntu,sans-serif;font-size:14px;color:#1d3a03}
.input-green{background:linear-gradient(var(--green-light),var(--green));border:1px solid var(--green-dark);color:var(--white);font-family:Ubuntu,sans-serif;font-size:14px;display:flex;align-items:center;padding-left:10px}
.hdiv{left:135px;top:675px;width:943px;border-top:1px dashed #999}
.photo-box{background:linear-gradient(135deg,#6b4a3a,#c99a82 50%,#7a5444);border:3px solid #7a0c05}
.join-label{position:absolute;left:80px;top:38px;font-family:"Cormorant Garamond",serif;font-style:italic;font-weight:600;font-size:32px;color:#111}
.video{left:466px;top:706px;width:175px;height:140px;background:#222;padding:4px}
.video-frame{height:115px;background:linear-gradient(#dfe7ea,#b9c6c9 60%,#6f7b7a)}
.video-bar{display:flex;align-items:center;gap:4px;height:17px;font-size:6px;color:#aaa;padding:0 4px}
.video-track{flex:1;height:4px;background:#666;border-radius:2px;position:relative}
.video-track i{position:absolute;left:0;top:0;height:4px;width:45%;background:#e0302a;border-radius:2px}
.cal-head{left:690px;top:686px;width:115px;display:flex;justify-content:space-between;align-items:center;font-family:Ubuntu,sans-serif;font-size:11px;color:#222}
.cal-arrow{width:11px;height:11px;border-radius:50%;background:#bbb}
.calendar{left:678px;top:706px;border-collapse:collapse;font-size:9px;color:#222}
.calendar th{height:16px;width:25.3px;background:linear-gradient(#fff,#ddd);border:1px solid #777;font-weight:700}
.calendar td{height:19.5px;border:1px solid #777;text-align:center}
.calendar td.hit span{display:inline-block;width:15px;height:15px;line-height:15px;border-radius:50%;background:#e0410e;color:#222}
.dl{left:892px;top:782px;width:165px;height:55px;border-radius:4px;background:linear-gradient(var(--green-light),var(--green) 60%,var(--green-dark));display:flex;align-items:center;justify-content:center;gap:12px;font-family:Ubuntu,sans-serif;font-weight:700;font-size:18px;color:#1d3a03}

/* footer */
.footer{left:0;top:855px;width:1200px;height:45px;background:linear-gradient(#8fd02a,var(--green) 70%,#4e960c);border-top:1px solid #cfe9a8}
.copy{left:470px;top:872px;font-family:Ubuntu,sans-serif;font-size:11px;color:#233}
.f-social{position:absolute;top:863px;height:27px;display:flex;align-items:center}
.f-social .sq{width:30px;height:30px;background:var(--white);border:1px solid #9ab}
.f-social .lbl{height:21px;display:flex;align-items:center;padding-left:14px;font-family:Ubuntu,sans-serif;font-weight:500;font-size:12px;color:var(--white)}
</style>
</head>
<body>

<header>
  <div class="abs brand">
    <div class="brand-row"><span class="brand-dot"></span><span class="brand-name">Peartreegrove</span></div>
    <div class="brand-tag">BALANCED NUTRITION, MIND, AND FITNESS</div>
  </div>
  <nav class="abs nav">
    <a href="#">YOUR COACHING<br>PROGRAM</a>
    <a href="#">WHY A<br>HEALTH COACH</a>
    <a href="#" class="current">ABOUT YOUR<br>COACH</a>
    <a href="#">RECIPES</a>
    <a href="#">BODY &amp; MIND<br>WORKOUTS</a>
  </nav>
  <svg class="abs nav-pointer" width="14" height="8"><path d="M0 0h14L7 7z" fill="#3a0a00"/></svg>
</header>

<section class="abs band"></section>
<div class="abs hero">
  <div class="hero-photo" role="img" aria-label="Woman in sportswear doing an abdominal leg-raise exercise on a mat in a bright studio"></div>
  <p class="hero-quote"><span class="mark">“</span>Body is your temple.<br>Keep it pure and clean<br>for the soul to reside in.<span class="mark">”</span></p>
</div>
<svg class="abs hero-pointer" width="22" height="14"><path d="M0 0h22L11 13z" fill="#6e0c05"/></svg>

<form class="abs signup">
  <h2>Sign Up</h2>
  <div class="field" style="top:56px">
    <svg width="11" height="11"><circle cx="5.5" cy="3.5" r="3" fill="#777"/><path d="M0 11a5.5 4 0 0 1 11 0z" fill="#777"/></svg>Name
    <svg class="end" width="14" height="12"><path d="M1 6l4 4 8-9" stroke="#2e8b1e" stroke-width="2.5" fill="none"/></svg>
  </div>
  <div class="field" style="top:103px">
    <svg width="12" height="9"><rect width="12" height="9" fill="#777"/><path d="M0 0l6 5 6-5" stroke="#fff" fill="none"/></svg>Name@email.com
    <svg class="end" width="11" height="11"><path d="M1 1l9 9M10 1l-9 9" stroke="#8a2a0a" stroke-width="2.5"/></svg>
  </div>
  <div class="field" style="top:149px">
    <svg width="11" height="11"><circle cx="7.5" cy="3.5" r="3" fill="#777"/><path d="M6 5L1 10" stroke="#777" stroke-width="2"/></svg>••••••••
  </div>
  <div class="social">
    <span class="s-friend"><i class="s-box"></i>Sign up with Friendloom</span>
    <span class="s-chirp"><i class="s-box"></i>Sign up with Chirpwell</span>
    <span class="continue">Continue <svg width="5" height="7"><path d="M0 0l5 3.5L0 7z" fill="#3a1500"/></svg></span>
  </div>
</form>

<a class="abs join" href="#">
  <div class="lead">Enjoy life to the fullest</div>
  <div class="cta">JOIN US NOW <svg width="22" height="24"><path d="M0 0l22 12L0 24z" fill="#fff"/></svg></div>
</a>

<section class="abs strip"></section>
<div class="thumb" style="left:142px;background:linear-gradient(135deg,#c0301a,#e9a020 50%,#5a8a1a)" role="img" aria-label="Platter of fresh fruits and vegetables"></div>
<div class="thumb" style="left:215px;background:linear-gradient(#f6f2ee,#e8ddd2)" role="img" aria-label="Woman doing an abdominal exercise"></div>
<div class="thumb" style="left:287px;background:linear-gradient(135deg,#3a6aa8,#d0a080 50%,#2a3a5a)" role="img" aria-label="Group of happy friends outdoors"></div>
<div class="thumb" style="left:363px;background:linear-gradient(#eeeeee,#c9c9c9)" role="img" aria-label="Woman stretching in a studio"></div>
<p class="abs strip-text">Exercise reduces <em>Stress</em>....</p>
<p class="abs auth">LOGIN<b></b>SIGN UP</p>

<main>
  <h3 class="abs h-col" style="left:130px;top:517px">Welcome to Peartreegrove !</h3>
  <p class="abs lead-o" style="left:135px;top:552px;width:290px">Sed posuere ligula rhoncus erat. Fusce urna dui, sollicitudin ac, pulvinar quis, tincidunt et, risus.</p>
  <p class="abs body-s" style="left:135px;top:580px;width:300px">Morbi volutpat leo in ligula. Integer vel magna. Nam justo augue, dictum a, hendrerit in, ultricies in, leo. NullamMorbi volutpat leo in ligula. Integer vel magna. Quisque ut magna et nisi bibendum sagittis. Fusce elit ligula</p>
  <a class="abs btn-green" style="left:228px;top:640px;width:181px;height:28px" href="#">Contact your Health Coach</a>

  <div class="abs vdiv" style="left:455px;top:518px;height:140px"></div>
  <h3 class="abs h-col" style="left:467px;top:517px">Testimonials</h3>
  <p class="abs body-s" style="left:470px;top:552px;width:180px;color:#333">At vero eos et accusamus et iusto odio tium voluptatum deleniti atque uri sint occaecati cupiditate.<br><b>Daniel Marsh</b><br>Managing Director</p>
  <a class="abs btn-green" style="left:531px;top:639px;width:116px;height:28px" href="#">Read More &gt;&gt;</a>

  <div class="abs vdiv" style="left:660px;top:518px;height:140px"></div>
  <h3 class="abs h-col" style="left:673px;top:517px">Latest on my blog:</h3>
  <p class="abs body-s" style="left:679px;top:552px;width:180px;color:#333">Welcome! This is my new blog!<br>I finally set up my new blog.<br>If you like it, subscribe to<br>my RSS feed!</p>
  <a class="abs btn-green" style="left:744px;top:640px;width:117px;height:28px" href="#">Read More &gt;&gt;</a>

  <div class="abs vdiv" style="left:875px;top:518px;height:140px"></div>
  <h3 class="abs h-side" style="left:888px;top:522px">NEWSLETTER</h3>
  <p class="abs" style="left:888px;top:550px;width:190px;font-family:Ubuntu,sans-serif;font-weight:500;font-size:12.5px;line-height:14px;color:#222">Sign-up for our free newsletter for all of our updates at Peartreegrove !</p>
  <div class="abs input-green" style="left:883px;top:597px;width:185px;height:30px">Email Address</div>
  <a class="abs input-green" style="left:883px;top:636px;width:76px;height:30px" href="#">Submit</a>

  <div class="abs hdiv"></div>

  <h3 class="abs h-col" style="left:136px;top:677px">Lets Build a Happy Community</h3>
  <div class="abs photo-box" style="left:138px;top:706px;width:303px;height:142px" role="img" aria-label="Many hands stacked together as a team">
    <span class="join-label">Join now</span>
  </div>

  <h3 class="abs h-col" style="left:466px;top:677px">Latest Videos</h3>
  <div class="abs video">
    <div class="video-frame" role="img" aria-label="Fitness class doing a balance pose in a bright studio"></div>
    <div class="video-bar">
      <svg width="6" height="7"><path d="M0 0l6 3.5L0 7z" fill="#ccc"/></svg>
      <span class="video-track"><i></i></span>
      <span>0:42 / 3:10</span>
    </div>
  </div>

  <div class="abs cal-head"><span class="cal-arrow"></span>August 2012<span class="cal-arrow"></span></div>
  <table class="abs calendar">
    <tr><th>S</th><th>M</th><th>T</th><th>W</th><th>T</th><th>F</th><th>S</th></tr>
    <tr><td></td><td></td><td></td><td></td><td></td><td>1</td><td>2</td></tr>
    <tr><td>3</td><td>4</td><td class="hit"><span>5</span></td><td>6</td><td>7</td><td>8</td><td>9</td></tr>
    <tr><td>10</td><td>11</td><td>12</td><td>13</td><td>14</td><td>15</td><td>16</td></tr>
    <tr><td class="hit"><span>17</span></td><td class="hit"><span>18</span></td><td>19</td><td>20</td><td>21</td><td>22</td><td>23</td></tr>
    <tr><td>24</td><td>25</td><td>26</td><td class="hit"><span>27</span></td><td>28</td><td>29</td><td>30</td></tr>
    <tr><td class="hit"><span>31</span></td><td></td><td></td><td></td><td></td><td></td><td></td></tr>
  </table>

  <h3 class="abs h-side" style="left:886px;top:687px">HEALTH HISTORY FORM</h3>
  <p class="abs" style="left:891px;top:711px;width:180px;font-family:Ubuntu,sans-serif;font-weight:500;font-size:12px;line-height:16px;color:#222">Schedule an appointment by filling the form and sending us.</p>
  <p class="abs" style="left:894px;top:759px;font-family:Ubuntu,sans-serif;font-weight:500;font-size:12px;color:#222;text-decoration:underline">Click Below to Download Form</p>
  <a class="abs dl" href="#">
    <svg width="34" height="26"><path d="M8 22a7 7 0 0 1 0-14 10 10 0 0 1 19 2 6 6 0 0 1 0 12z" fill="#1d3a03"/><path d="M17 9v10M12 15l5 5 5-5" stroke="#7cc51f" stroke-width="3" fill="none"/></svg>Download
  </a>
</main>

<footer>
  <div class="abs footer"></div>
  <p class="abs copy">Copyright 2012 - All Rights Reserved</p>
  <div class="f-social" style="left:687px"><span class="sq"></span><span class="lbl" style="width:155px;background:#3d5a9a">Add me on Friendloom</span></div>
  <div class="f-social" style="left:890px"><span class="sq"></span><span class="lbl" style="width:157px;background:#3aaee0">Follow me on Chirpwell</span></div>
</footer>

</body>
</html>
```